手延うどん(乾麺)のパッケージデザイン(製品袋)を依頼させて頂きます。和紙系か和紙雲竜系の袋を考えていますので高級感のあるデザインを希望します。ターゲット層は40-60代の価格ではなく美味しさを求めているお客様。何本か並べると綺麗なデザイン。※現在販売しているデザインだと、シンプルすぎるかなと感じています。
サイズ:W50×D27×H25mm
参考に現在のデザイン写真を添付しておきます。
サイズが間違っていました。横50mm、縦270mm、厚み25mmです。
新たな写真を添付致しました。

和のイメージと背景の小麦のデザイン。温故知新も決め手のポイントでした。

今回、たくさんのデザイン案ありがとうございました。ヨツバリオさんを通してお願いしたのが初めてで、選ぶのに苦労しました・・・。次回もお願いしようと考えているので、機会がございましたら、またよろしくお願い致します。

```html
<!DOCTYPE html>
<html lang="ja">
<head>
<meta charset="utf-8">
<title>上州 手延うどん パッケージ</title>
<link rel="stylesheet" href="https://fonts.googleapis.com/css2?family=Shippori+Mincho:wght@700&family=Yuji+Boku&display=swap">
<style>
  :root {
    --paper: #f4f1e8;
    --paper-shade: #e8e3d5;
    --frame: #cfcac0;
    --gold-light: #dcc67e;
    --gold: #b8973e;
    --gold-dark: #8c6d22;
    --ink: #1c1714;
    --seal: #b3121b;
    --silver: #a9a9a6;
    --label-text: #ffffff;
  }
  html, body {
    margin: 0;
    padding: 0;
    width: 1200px;
    height: 4768px;
    overflow: hidden;
    background: #ffffff;
  }
  .package {
    position: relative;
    width: 1200px;
    height: 4768px;
    background: radial-gradient(ellipse at 50% 30%, var(--paper) 0%, var(--paper-shade) 100%);
    overflow: hidden;
  }
  .package__frame {
    position: absolute;
    inset: 36px;
    border: 6px solid var(--frame);
    pointer-events: none;
  }
  .origin-label {
    position: absolute;
    left: 488px;
    top: 0;
    width: 224px;
    height: 520px;
    background: linear-gradient(180deg, var(--gold-light) 0%, var(--gold) 55%, var(--gold-dark) 100%);
    display: flex;
    align-items: center;
    justify-content: center;
  }
  .origin-label__text {
    writing-mode: vertical-rl;
    font-family: "Shippori Mincho", serif;
    font-weight: 700;
    font-size: 120px;
    line-height: 1;
    letter-spacing: 4px;
    color: var(--label-text);
    margin: 0;
  }
  .brush-rings {
    position: absolute;
    left: 150px;
    top: 2820px;
    width: 900px;
    height: 1800px;
  }
  .product-title {
    position: absolute;
    left: 0;
    top: 700px;
    width: 1200px;
    display: flex;
    justify-content: center;
    margin: 0;
  }
  .product-title__text {
    writing-mode: vertical-rl;
    font-family: "Yuji Boku", serif;
    font-weight: 400;
    line-height: 1;
    color: var(--ink);
    margin: 0;
  }
  .product-title__method {
    display: block;
    font-size: 340px;
    letter-spacing: 40px;
  }
  .product-title__noodle {
    display: block;
    font-size: 470px;
    letter-spacing: -10px;
  }
  .brand-seal {
    position: absolute;
    left: 380px;
    top: 3080px;
    width: 140px;
    height: 170px;
    background: var(--seal);
  }
</style>
</head>
<body>
  <main class="package">
    <div class="package__frame"></div>

    <div class="origin-label">
      <p class="origin-label__text">上州</p>
    </div>

    <svg class="brush-rings" viewBox="0 0 900 1800" role="img" aria-label="金色と銀色の筆で描いた円の飾り">
      <defs>
        <radialGradient id="ringTone" cx="50%" cy="45%" r="55%">
          <stop offset="0%" stop-color="#d8c27a" stop-opacity="0.1"/>
          <stop offset="55%" stop-color="#b8973e" stop-opacity="0.4"/>
          <stop offset="100%" stop-color="#a9a9a6" stop-opacity="0.3"/>
        </radialGradient>
      </defs>
      <ellipse cx="450" cy="900" rx="440" ry="880" fill="url(#ringTone)"/>
    </svg>

    <h1 class="product-title">
      <span class="product-title__text">
        <span class="product-title__method">手延</span>
        <span class="product-title__noodle">うどん</span>
      </span>
    </h1>

    <div class="brand-seal" role="img" aria-label="朱色の落款印"></div>
  </main>
</body>
</html>
```